Web page for a garment manufacturing company

We are clothing manufacturer based in Romania.
With our recent expansion, we have significantly increased our internal capacity, allowing us to take on new partnerships and deliver high-quality production services.
Our expertise includes producing classic coats, blazers, trousers, skirts, dresses, and blouses, though we are flexible and open to working with various other textile products.

Target Market(s)

High-end market and luxury

Industry/Entity Type

Garments Manufacturer

Coding

Coded - Design and coding required

Number of Pages Required

1 page

Colors

Designer to choose only greyscale colors for use in the design.

Requirements
Must have
• Velmora logo from our presentation
Nice to have
• https://www.dornalo.pt/
Should not have
• prices, wedding dresses, collections

```html
<!DOCTYPE html>
<html lang="en">
<head>
<meta charset="utf-8">
<title>Velmora — Garment Manufacturing</title>
<link href="https://fonts.googleapis.com/css2?family=Cormorant+Garamond:wght@500;600&family=Libre+Baskerville&family=Raleway:wght@400;500;600;700&display=swap" rel="stylesheet">
<style>
:root{
  --ink:#111;
  --text:#333;
  --muted:#777;
  --line:#e2e2e2;
  --frame:#ededed;
  --paper:#fff;
  --soft:#f6f6f6;
}
*{box-sizing:border-box;margin:0;padding:0}
html,body{width:1200px;height:3116px;overflow:hidden;background:var(--paper)}
body{font-family:'Raleway',sans-serif;color:var(--text);position:relative}
.abs{position:absolute}
.header{left:0;top:0;width:1200px;height:88px;text-align:center}
.logo{font-family:'Cormorant Garamond',serif;font-weight:600;font-size:30px;color:var(--ink);padding-top:10px;letter-spacing:.5px}
.nav{display:flex;justify-content:center;gap:26px;margin-top:8px;font-size:10px;font-weight:600;letter-spacing:1px;color:var(--muted)}
.nav .active{color:var(--ink);border-bottom:2px solid var(--ink);padding-bottom:3px}
.hero{left:0;top:88px;width:1200px;height:660px;background:linear-gradient(180deg,#7d8b94 0%,#4c5a63 40%,#2f3a40 75%,#3c3833 100%)}
.hero-copy{right:70px;top:232px;width:380px;text-align:center;color:#fff}
.hero-copy h1{font-size:40px;font-weight:600;letter-spacing:.5px}
.hero-copy p{font-size:18px;margin-top:10px;line-height:1.4}
.btn-outline{display:inline-block;margin-top:22px;border:1px solid #fff;padding:7px 26px;font-size:10px;letter-spacing:1.5px}
.section-title{width:1200px;left:0;text-align:center;font-size:14px;font-weight:700;letter-spacing:1.5px;color:var(--ink)}
.section-title::after{content:"";display:block;width:40px;height:1px;background:var(--ink);margin:8px auto 0}
.cards{left:180px;width:840px;display:flex;gap:12px}
.card{width:272px}
.card .photo{height:160px;background:linear-gradient(135deg,#bdbdbd,#6e6e6e)}
.card h4{font-size:10px;font-weight:700;margin-top:10px;color:var(--ink)}
.card p{font-size:10px;color:var(--muted);margin-top:4px;line-height:1.4}
.dots{left:0;width:1200px;display:flex;justify-content:center;gap:6px}
.dots span{width:7px;height:7px;border-radius:50%;background:#ccc}
.dots span:first-child{background:#555}
.video{left:120px;top:1148px;width:952px;height:472px;background:linear-gradient(160deg,#9a9a9a 0%,#5a5a5a 55%,#3a3a3a 100%)}
.play{left:456px;top:216px}
.stats{left:0;top:1680px;width:1200px;height:320px;background:linear-gradient(90deg,#8c8c8c,#b5b5b5 45%,#6d6d6d)}
.stat-row{left:290px;top:124px;display:flex;gap:34px;color:#fff;text-align:center}
.stat-row b{display:block;font-size:40px;font-weight:500}
.stat-row span{font-size:14px}
.features{left:64px;top:2400px;width:1072px;height:240px}
.feature{position:absolute;border:10px solid var(--frame);background:var(--paper);text-align:center}
.feature .ico{width:36px;height:36px;border-radius:50%;background:var(--ink);margin:18px auto 8px;display:flex;align-items:center;justify-content:center}
.feature h3{font-family:'Libre Baskerville',serif;font-size:17px;font-weight:400;color:var(--ink)}
.feature p{font-size:9px;color:var(--muted);margin:8px 22px 0;line-height:1.5}
.feature.row{display:flex;align-items:center;text-align:left;gap:14px;padding:0 20px}
.feature.row .ico{margin:0;flex:none}
.perks{left:150px;top:2740px;width:900px;display:flex;justify-content:space-between;text-align:center;font-size:9px;color:var(--muted)}
.perks div{width:240px}
.perks b{display:block;width:18px;height:18px;border:1.5px solid #999;border-radius:50%;margin:0 auto 6px}
.footer{left:0;top:2860px;width:1200px;height:256px;border-top:1px solid var(--line)}
.newsletter{left:180px;top:26px;width:260px;font-size:10px}
.newsletter h5{font-size:10px;font-weight:700;color:var(--ink)}
.newsletter p{color:var(--muted);margin-top:6px}
.field{margin-top:24px;display:flex;justify-content:space-between;border-bottom:1px solid #999;padding-bottom:4px;color:var(--muted)}
.field b{color:var(--ink)}
.social{display:flex;gap:10px;margin-top:20px}
.social span{width:14px;height:14px;border-radius:50%;background:#444}
.links{top:26px;font-size:9px;line-height:2.2;color:var(--muted)}
.links h6{font-size:9px;color:var(--ink);font-weight:700}
</style>
</head>
<body>
<header class="abs header">
  <div class="logo">Velmora</div>
  <nav class="nav"><span class="active">HOME</span><span>ABOUT ▾</span><span>EXPERTISE ▾</span><span>SERVICES ▾</span><span>INDUSTRIES</span><span>GET IN TOUCH ▾</span></nav>
</header>

<section class="abs hero" role="img" aria-label="Model in a long red dress standing on seaside rocks">
  <div class="abs hero-copy">
    <h1>Star-Studded Looks</h1>
    <p>Light up every room with our stunning<br>and chic looks.</p>
    <span class="btn-outline">DISCOVER</span>
  </div>
</section>

<h2 class="abs section-title" style="top:776px">NEWS</h2>
<div class="abs cards" style="top:820px">
  <article class="card"><div class="photo" role="img" aria-label="Designer at a desk in the studio"></div><h4>Mara Ilescu</h4><p>"Our new line of tailored blazers is now in full production this season."</p></article>
  <article class="card"><div class="photo" role="img" aria-label="Team member in an office setting"></div><h4>Dorian Cole</h4><p>"We are proud of the craft our teams bring to every coat we make."</p></article>
  <article class="card"><div class="photo" role="img" aria-label="Partner smiling in a workshop"></div><h4>Ilinca Dobre</h4><p>"I trust their quality control from first sample to final delivery."</p></article>
</div>
<div class="abs dots" style="top:1052px"><span></span><span></span><span></span></div>

<section class="abs video" role="img" aria-label="Video still of a man in a red sweater seated on a city ledge">
  <svg class="abs play" width="40" height="40" viewBox="0 0 40 40"><circle cx="20" cy="20" r="20" fill="#fff"/><path d="M16 12 L29 20 L16 28 Z" fill="#222"/></svg>
</section>

<section class="abs stats" role="img" aria-label="Model in a floral dress by the sea">
  <div class="abs stat-row">
    <div><b>7000</b><span>Coats/Day</span></div>
    <div><b>8000</b><span>Coats/Day</span></div>
    <div><b>4000</b><span>Suits/Day</span></div>
    <div><b>5000</b><span>Trousers/Day</span></div>
    <div><b>1080</b><span>Dresses/Day</span></div>
  </div>
</section>

<h2 class="abs section-title" style="top:2050px">VELMORA UNIVERSE</h2>
<div class="abs cards" style="top:2080px">
  <article class="card"><div class="photo" role="img" aria-label="Designer at a desk in the studio"></div><h4>Mara Ilescu</h4><p>"Every garment leaves our floor checked by hand for fit and finish."</p></article>
  <article class="card"><div class="photo" role="img" aria-label="Team member in an office setting"></div><h4>Dorian Cole</h4><p>"Our expanded capacity lets us welcome new partners this year."</p></article>
  <article class="card"><div class="photo" role="img" aria-label="Partner smiling in a workshop"></div><h4>Ilinca Dobre</h4><p>"Flexible runs and fine fabrics made the whole project simple."</p></article>
</div>
<div class="abs dots" style="top:2346px"><span></span><span></span><span></span></div>

<section class="abs features">
  <div class="feature" style="left:0;top:0;width:320px;height:240px">
    <div class="ico"><svg width="16" height="16" viewBox="0 0 16 16"><path d="M3 8 L7 12 L13 4" stroke="#fff" stroke-width="2" fill="none"/></svg></div>
    <h3>100% Satisfaction Guaranteed</h3>
    <p>Every order is inspected before it ships, so you receive pieces made right.</p>
  </div>
  <div class="feature row" style="left:344px;top:0;width:384px;height:112px">
    <div class="ico"><svg width="16" height="16" viewBox="0 0 16 16"><path d="M4 2 L7 5 L5 7 Q7 10 9 11 L11 9 L14 12 L12 14 Q4 12 2 4 Z" fill="#fff"/></svg></div>
    <div><h3>24/7 Online Service</h3><p style="margin:6px 0 0">Our team answers your questions any time of day or night.</p></div>
  </div>
  <div class="feature row" style="left:344px;top:128px;width:384px;height:112px">
    <div class="ico"><svg width="16" height="16" viewBox="0 0 16 16"><path d="M2 8 H12 M8 4 L12 8 L8 12" stroke="#fff" stroke-width="2" fill="none"/></svg></div>
    <div><h3>Fast Delivery</h3><p style="margin:6px 0 0">Reliable lead times and shipping to partners across Europe.</p></div>
  </div>
  <div class="feature" style="left:752px;top:0;width:320px;height:240px">
    <div class="ico"><svg width="16" height="16" viewBox="0 0 16 16"><rect x="3" y="7" width="10" height="7" fill="#fff"/><path d="M5 7 V5 A3 3 0 0 1 11 5 V7" stroke="#fff" stroke-width="1.6" fill="none"/></svg></div>
    <h3>Payment With Secure System</h3>
    <p>Transactions are handled through a safe and trusted process.</p>
  </div>
</section>

<section class="abs perks">
  <div><b></b>Exclusive collections from leading designers</div>
  <div><b></b>Free shipping throughout Europe</div>
  <div><b></b>Free returns</div>
</section>

<footer class="abs footer">
  <div class="abs newsletter">
    <h5>Subscribe to our newsletter</h5>
    <p>Get news from our studio.</p>
    <div class="field"><span>Email</span><b>Subscribe</b></div>
    <div class="social"><span></span><span></span><span></span><span></span><span></span></div>
  </div>
  <div class="abs links" style="left:770px">
    <h6>Useful links</h6>
    <div>About us</div><div>Our expertise</div><div>Manufacturing</div><div>Industries</div><div>Sustainability</div><div>Contact</div><div>Careers</div>
  </div>
  <div class="abs links" style="left:910px">
    <h6>About us</h6>
    <div>About Velmora</div><div>Quality and certifications</div><div>Jobs</div>
  </div>
</footer>
</body>
</html>
```